Marlow Vane Lettings Web Site Design

I am after a very simple 3 page web site please. I attach a PDF with the text and information. The logo is also in the PDF. The colours should be orange and blues. The pages should be HOME - LANDLORDS - TENANTS.
Lettings and Property Management Company aimed at just being a reference point for tenants but more of a sales pitch to landlords. Please refer to the attached PDF and word file which contains far more content for the various pages.

Target Market(s)

Prospective Landlords mainly but tenants also

Industry/Entity Type

Lettings and Property Management

Number of Pages Required

3 page

Font styles to use
Sans Serif
Other font styles liked:
• Candara

Colors
0054AA
0677BA
7BADD7
CADEEF
E8F1F8
F0912C
F2A743
F7CA91
FBE8D2
FDF5EE

Requirements
Must have
• Must be colour co-ordinated to the logo (orange and dark blue predominently, Must have good quality stock images relating to property and renting out property. Should have home page and links to landlord page and tenant page. Must have the 4 logos that we are affiliated to (TKR, Housing Settle, BWN and Tenure Funds Guard) - all attached.
Nice to have
• Modern feel, crisp and sharp but simple - good stock images.

```html
<!DOCTYPE html>
<html lang="en">
<head>
<meta charset="utf-8">
<title>Marlow Vane Lettings – Home</title>
<link href="https://fonts.googleapis.com/css2?family=Figtree:wght@300;400;500;600;700&display=swap" rel="stylesheet">
<style>
:root{
  --navy:#1d3566;
  --navy-deep:#1e3a6e;
  --sky:#1a9fd0;
  --orange:#e8891d;
  --band:#f0f4f8;
  --ink:#5b5f66;
  --badge:#d5dde7;
  --white:#ffffff;
}
*{box-sizing:border-box;margin:0;padding:0}
html,body{width:854px;height:1200px;overflow:hidden;background:var(--white);font-family:"Figtree",sans-serif}
.page{position:relative;width:854px;height:1200px}
.hero{position:absolute;left:0;top:0;width:854px;height:576px;
  background:radial-gradient(ellipse at 55% 40%,#8a6f62 0%,#4f5a6e 40%,#2c3a52 75%,#1f2b40 100%)}
.hero-shade{position:absolute;inset:0;background:linear-gradient(180deg,rgba(20,30,50,.15) 0%,rgba(20,30,50,.45) 100%)}
.brand{position:absolute;left:122px;top:62px;display:flex;align-items:center;gap:9px;color:var(--white);font-weight:600;font-size:16px;line-height:18px;letter-spacing:.8px}
.brand-dot{width:18px;height:18px;border-radius:50%;background:var(--orange);flex:none}
.nav{position:absolute;top:46px;left:507px;display:flex;gap:15px;font-size:8.6px;font-weight:700}
.nav a{color:var(--white);text-decoration:none}
.nav a.active{color:var(--sky)}
.hero-title{position:absolute;left:0;width:854px;top:364px;text-align:center;color:var(--white);font-weight:500;font-size:42px;line-height:38px;letter-spacing:-1.3px}
.hero-sub{position:absolute;left:0;width:854px;top:457px;text-align:center;color:var(--white);font-weight:600;font-size:11px}
.hero-link{position:absolute;left:0;width:854px;top:483px;text-align:center;font-size:8.2px;font-weight:700}
.hero-link a{color:var(--orange)}
.scroll{position:absolute;left:407px;top:517px;width:40px;height:59px}
.scroll-label{position:absolute;left:0;width:854px;top:543px;text-align:center;color:var(--white);font-size:6.2px;font-weight:700}
.affiliates{position:absolute;left:0;top:576px;width:854px;height:101px;background:var(--band)}
.affiliates p{position:absolute;top:20px;width:854px;text-align:center;color:var(--ink);font-size:10.2px;font-weight:300}
.badge{position:absolute;background:var(--badge);border-radius:3px}
.about-label{position:absolute;left:121px;top:728px;display:flex;align-items:center;gap:6px;color:var(--sky);font-size:9.6px;font-weight:700}
.about-label::before{content:"";width:32px;height:1px;background:var(--orange)}
.about-heading{position:absolute;left:313px;top:724px;width:440px;color:var(--navy);font-weight:600;font-size:16.4px;line-height:21.4px;letter-spacing:-.5px;white-space:nowrap}
.family-photo{position:absolute;left:121px;top:828px;width:312px;height:288px;background:linear-gradient(135deg,#c9b8a6 0%,#8e7a6a 45%,#3c4a66 100%)}
.about-body{position:absolute;left:477px;top:853px;width:270px;color:var(--ink);font-size:10px;line-height:15px;font-weight:300;white-space:nowrap}
.about-body p{margin-bottom:15px}
.about-body .emphasis{font-size:11.4px;line-height:15px;font-weight:500;margin-top:20px}
.btn{position:absolute;left:477px;top:1055px;width:124px;height:32px;background:var(--orange);color:var(--white);font-size:7.8px;font-weight:700;display:flex;align-items:center;justify-content:center;border-radius:2px;letter-spacing:.2px}
.footer{position:absolute;left:0;top:1169px;width:854px;height:31px;background:var(--navy-deep);color:var(--white);font-size:9.6px}
.footer .copy{position:absolute;left:121px;top:9px}
.footer .links{position:absolute;right:124px;top:9px;display:flex;gap:11px}
</style>
</head>
<body>
<div class="page">
  <section class="hero" role="img" aria-label="Photo of a smiling couple being shown a property by a letting agent holding a clipboard">
    <div class="hero-shade"></div>
  </section>
  <div class="brand"><span class="brand-dot"></span><span>MARLOW VANE<br>LETTINGS</span></div>
  <nav class="nav">
    <a class="active" href="#">HOME</a>
    <a href="#">LANDLORDS</a>
    <a href="#">TENANTS</a>
    <a href="#">CONTACT US</a>
  </nav>
  <h1 class="hero-title">Stress-Free Lettings and<br>Property Management</h1>
  <p class="hero-sub">Professional tenant sourcing, full management, and maintenance handled end-to-end.</p>
  <p class="hero-link"><a href="#">ACTIVELY LOOKING FOR NEW LANDLORDS</a></p>
  <svg class="scroll" viewBox="0 0 40 59">
    <line x1="20" y1="0" x2="20" y2="8" stroke="#fff" stroke-width=".8"/>
    <rect x="15.5" y="10.5" width="9" height="13" rx="4.5" fill="none" stroke="#fff" stroke-width=".9"/>
    <line x1="20" y1="13.5" x2="20" y2="16" stroke="#fff" stroke-width="1"/>
    <line x1="20" y1="37" x2="20" y2="59" stroke="#fff" stroke-width=".8"/>
  </svg>
  <div class="scroll-label">SCROLL</div>

  <section class="affiliates">
    <p>We are members of or affiliated to</p>
    <div class="badge" role="img" aria-label="TKR membership badge" style="left:262px;top:38px;width:38px;height:41px"></div>
    <div class="badge" role="img" aria-label="Housing Settle membership badge" style="left:318px;top:46px;width:80px;height:24px"></div>
    <div class="badge" role="img" aria-label="BWN registration badge" style="left:413px;top:41px;width:39px;height:34px"></div>
    <div class="badge" role="img" aria-label="Tenure Funds Guard membership badge" style="left:467px;top:45px;width:122px;height:26px"></div>
  </section>

  <div class="about-label">ABOUT THE COMPANY</div>
  <h2 class="about-heading">Marlow Vane Lettings has emerged after over 20 years<br>of privately managing our own rental properties. We are<br>family run and decided to move all of our properties under<br>one ‘umbrella’.</h2>

  <div class="family-photo" role="img" aria-label="Photo of a happy family sitting under a cardboard roof in their new home"></div>
  <div class="about-body">
    <p>Now professionally set up as a legal entity, Marlow<br>Vane is looking to welcome new tenants and landlords<br>to an innovative and fresh way of letting property.</p>
    <p>We always maintain a high standard of service and our<br>friendly and helpful team are experienced in all areas<br>and offer an excellent service in helping landlords and<br>tenants deal with problems and issues they face daily.</p>
    <p class="emphasis">Out of hours emergency service which means<br>we are there (in an emergency) for our tenants<br>and landlords 24/7.</p>
  </div>
  <a class="btn">LANDLORD ENQUIRY</a>

  <footer class="footer">
    <span class="copy">© 2025 Marlow Vane Lettings All Rights Reserved</span>
    <span class="links"><span>Disclaimer</span><span>Privacy Policy</span><span>Terms &amp; Condition</span></span>
  </footer>
</div>
</body>
</html>
```